New business card for a regional office of a US M&A company

We need business card for a finance company, office based in Hong Kong , our Head office is in US, our business is to Merge and acquires companies , the new office will be a regional office for the Asia Pacific region. We want to use the head office logo as attached ( but don't have to be exactly the same, can be a variation to it) as a base and then add Asia Pacific alongside the logo.
We would prefer to have be bilingual Eng + Chinese, although we don't really have Chinese company name .

Industry/Entity Type

Business

Contact Information for Business Card

Carla Beth Soren
 

VP,
APAC M&A Operations
Tovar Crest Asia Pacific Limited
 
Unit 1407, K82
27 Sai Lok Fung Road, 
Hong Kong 
 
M: +852 6481 2037
T : +852 2736 4100
F : +852 2736 4155
VOIP: 4813
 
cbsoren@tovarcrest.com

Font styles to use
Serif
Sans Serif

Colors

Designer to choose colors to be used in the design.

Requirements
Must have
• APAC Office

```html
<!DOCTYPE html>
<html lang="en">
<head>
<meta charset="utf-8">
<title>Tovar Crest Asia Pacific — Business Card</title>
<link href="https://fonts.googleapis.com/css2?family=Crimson+Text:wght@400&family=Montserrat:wght@400;600;700&display=swap" rel="stylesheet">
<style>
  :root {
    --navy: #0d2a47;
    --accent: #1f9fc4;
    --ink: #3a3f45;
    --paper: #f4f4f4;
    --paper-shade: #e9e9ea;
    --map-dot: #dcdde0;
    --backdrop: #2b2b2d;
  }
  * { box-sizing: border-box; margin: 0; padding: 0; }
  html, body { width: 1200px; height: 834px; overflow: hidden; }
  body {
    background: var(--backdrop);
    font-family: "Montserrat", Arial, sans-serif;
    position: relative;
  }
  .card {
    position: absolute;
    width: 520px;
    height: 300px;
    background: linear-gradient(135deg, #fafafa 0%, var(--paper) 55%, var(--paper-shade) 100%);
    overflow: hidden;
    box-shadow: 0 10px 30px rgba(0,0,0,.45);
  }
  .card--front { left: 70px; top: 90px; }
  .card--back { left: 610px; top: 444px; }

  .world-map {
    position: absolute; inset: 0;
    background:
      radial-gradient(ellipse 22% 26% at 22% 34%, var(--map-dot) 0%, transparent 70%),
      radial-gradient(ellipse 14% 30% at 40% 70%, var(--map-dot) 0%, transparent 70%),
      radial-gradient(ellipse 30% 22% at 66% 28%, var(--map-dot) 0%, transparent 70%),
      radial-gradient(ellipse 12% 12% at 82% 72%, var(--map-dot) 0%, transparent 70%);
    opacity: .8;
  }

  .top-tab {
    position: absolute; top: 0; left: 57%;
    width: 19%; height: 12px;
    background: var(--navy);
    border-bottom: 3px solid var(--accent);
  }

  .brand-block {
    position: absolute;
    background: var(--navy);
    border-bottom: 3px solid var(--accent);
    display: flex; flex-direction: column;
    align-items: center; justify-content: center;
    gap: 10px;
  }
  .card--front .brand-block { right: 10%; bottom: 12%; width: 34%; height: 30%; }
  .card--back .brand-block { left: 6%; top: 41%; width: 34%; height: 31%; }
  .brand-mark {
    width: 16px; height: 16px;
    background: var(--accent);
  }
  .brand-name {
    font-family: "Montserrat", Arial, sans-serif;
    font-weight: 700;
    font-size: 20px;
    letter-spacing: .5px;
    color: var(--accent);
    white-space: nowrap;
  }

  .rule {
    position: absolute; left: 48%; right: 0; top: 27%;
    height: 1.5px; background: var(--accent);
  }
  .contact {
    position: absolute; left: 48%; top: 28%;
    color: var(--ink);
  }
  .person-name {
    font-family: "Crimson Text", Georgia, serif;
    font-size: 19px; color: #444;
    margin-top: 2px;
  }
  .person-title {
    font-size: 11.5px; color: var(--accent);
    padding-bottom: 6px;
    border-bottom: 1.5px solid var(--accent);
    width: 185px;
  }
  .company {
    font-size: 10.5px; font-weight: 700; color: var(--accent);
    margin-top: 6px;
  }
  .address {
    font-style: normal; font-size: 10.5px; line-height: 1.35;
    margin: 3px 0 0 10px;
  }
  .phones {
    list-style: none; font-size: 10.5px; line-height: 1.4;
    margin: 10px 0 0 22px;
  }
  .phones li { display: flex; align-items: center; gap: 8px; }
  .phones svg { width: 9px; height: 9px; fill: none; stroke: var(--accent); stroke-width: 1.4; }
  .voip { font-size: 10.5px; margin: 6px 0 0 39px; }
</style>
</head>
<body>

  <section class="card card--front" aria-label="Card front">
    <div class="world-map" role="img" aria-label="Faint dotted world map background"></div>
    <div class="top-tab"></div>
    <div class="brand-block">
      <span class="brand-mark"></span>
      <span class="brand-name">TOVAR CREST</span>
    </div>
  </section>

  <section class="card card--back" aria-label="Card back">
    <div class="world-map" role="img" aria-label="Faint dotted world map background"></div>
    <div class="brand-block">
      <span class="brand-mark"></span>
      <span class="brand-name">TOVAR CREST</span>
    </div>
    <div class="rule"></div>
    <div class="contact">
      <h1 class="person-name">Carla Beth Soren</h1>
      <p class="person-title">VP, APAC M&amp;A Operations</p>
      <p class="company">Tovar Crest Asia Pacific Limited</p>
      <address class="address">Unit 1407, K82<br>27 Sai Lok Fung Road,<br>Hong Kong</address>
      <ul class="phones">
        <li><svg viewBox="0 0 10 10"><rect x="2.5" y="0.8" width="5" height="8.4" rx="1"/></svg>+852 6481 2037</li>
        <li><svg viewBox="0 0 10 10"><circle cx="5" cy="5" r="4"/><path d="M1 5h8M5 1v8"/></svg>+852 2736 4100</li>
        <li><svg viewBox="0 0 10 10"><rect x="1" y="4" width="8" height="4.5" rx="0.8"/><path d="M3 4V1.2h4V4"/></svg>+852 2736 4155</li>
      </ul>
      <p class="voip">VOIP 4813</p>
    </div>
  </section>

</body>
</html>
```